Gravel Ale Label design/Graphic design

The Company
Gravel ale is an exciting new brand of ‘fit beer’ targeted at fitness enthusiasts as well as beer lovers. Gravel ale is a craft beer with added protein which can be used as a post work out recovery/leisure beverage. The target audience is generally male, 18-30 years old.
We need label/graphic design of the product to appear on our website www.gravelale-demo.co.uk

The Project
The project is to submit four designs, one for each flavour:
• Larger
• Honey Ale
• Banana Ale
• Zero Alcohol

The design of each flavour must be differentiated, yet have a consistent theme throughout all flavours. At this point Gravel ale has no official logo so feel free to incorporate this into the design, although this is not absolutely necessary.

The label/design should include the following basic information:
Brand name: Gravel Ale
Type: Larger/Honey Ale/Banana Ale/Zero
Tag: 7g High Quality Protein
Alcohol percentage: 4%/Vol (0%/Vol for the Zero alcohol version)
Volume: 300ml

Brand Guidelines (designs not necessarily limited to these)
Font: Aldrich
Main Colours: Blue # 005fbf Orange # ed7000
Basic beer bottle image attached.

The final design will be displayed on (but not limited to) the website www.gravelale-demo.co.uk

The winning designer may be contacted for future projects and opportunities with Gravel Ale.
Updates

Project Deadline Extended
Reason: My apologies I have been sick the last few days and have been unable to provide feedback. Your work is much appreciated, I will extend the project to give us a little more time and provide feedback individually later today. Best Regards, Oliver

Target Market(s)

The target audience is generally male, 18-30 years old.

Industry/Entity Type

Fitness

Requirements
Must have
• The label/design should include the following basic information:
Brand name: Gravel Ale
Volume: 300ml

```html
<!DOCTYPE html>
<html lang="en">
<head>
<meta charset="utf-8">
<title>Gravel Ale – Label Range</title>
<link rel="stylesheet" href="https://fonts.googleapis.com/css2?family=Playfair+Display:wght@700;900&family=Josefin+Sans:wght@300;400&family=Roboto:wght@700&display=swap">
<style>
  :root {
    --bg: #ffffff;
    --glass-light: #d98a2e;
    --glass-mid: #a5560f;
    --glass-dark: #2a1405;
    --cap: #8a7a2a;
    --banana: #ee7203;
    --ink: #111111;
    --honey-band: #8fd4c4;
    --honey-fill: #5ea9a6;
    --honey-line: #243447;
    --honey-ink: #2f5d63;
    --lager-blue: #185c9e;
    --lager-ring: #d9d9d9;
    --zero-red: #a0202c;
    --white: #ffffff;
  }
  html, body {
    margin: 0;
    width: 1200px;
    height: 900px;
    overflow: hidden;
    background: var(--bg);
  }
  .range { display: block; width: 1200px; height: 900px; }
  .serif { font-family: "Playfair Display", serif; font-weight: 900; }
  .sans-light { font-family: "Josefin Sans", sans-serif; font-weight: 300; }
  .sans-bold { font-family: "Roboto", sans-serif; font-weight: 700; }
  .ink { fill: var(--ink); }
  .honey-ink { fill: var(--honey-ink); }
  .white { fill: var(--white); }
  .red { fill: var(--zero-red); }
  .zero-frame { fill: none; stroke: var(--zero-red); stroke-width: 2; opacity: .75; }
</style>
</head>
<body>
<svg class="range" viewBox="0 0 1200 900" xmlns="http://www.w3.org/2000/svg">
  <defs>
    <linearGradient id="glass" x1="0" x2="1" y1="0" y2="0">
      <stop offset="0" stop-color="var(--glass-dark)"/>
      <stop offset=".2" stop-color="var(--glass-mid)"/>
      <stop offset=".5" stop-color="var(--glass-light)"/>
      <stop offset=".8" stop-color="var(--glass-mid)"/>
      <stop offset="1" stop-color="var(--glass-dark)"/>
    </linearGradient>
    <symbol id="bottle" viewBox="-4 0 178 676" overflow="visible">
      <rect x="48" y="0" width="74" height="16" rx="3" fill="var(--cap)"/>
      <path d="M50,15 H120 V30 Q118,35 118,45 L120,190 Q122,260 160,300 Q172,315 172,340 L170,650 Q170,672 150,672 H20 Q0,672 0,650 L-2,340 Q-2,315 10,300 Q48,260 50,190 L52,45 Q52,35 50,30 Z" fill="url(#glass)"/>
    </symbol>
  </defs>

  <!-- Bottles -->
  <g role="img" aria-label="Photographed amber beer bottle">
    <use href="#bottle" x="65" y="208" width="170" height="672"/>
  </g>
  <g role="img" aria-label="Photographed amber beer bottle">
    <use href="#bottle" x="365" y="208" width="170" height="672"/>
  </g>
  <g role="img" aria-label="Photographed amber beer bottle">
    <use href="#bottle" x="665" y="208" width="170" height="672"/>
  </g>
  <g role="img" aria-label="Photographed amber beer bottle">
    <use href="#bottle" x="965" y="208" width="170" height="672"/>
  </g>

  <!-- Banana Ale label -->
  <g class="label label-banana">
    <path d="M90,757 V552 A60.5,60 0 0 1 211,552 V757 Z" fill="var(--banana)"/>
    <text class="serif ink" x="150" y="555" font-size="22" text-anchor="middle">Gravel</text>
    <text class="serif ink" x="150" y="577" font-size="22" text-anchor="middle">Ale</text>
    <text class="serif ink" x="150" y="612" font-size="14" text-anchor="middle">Banana Ale</text>
    <text class="serif ink" x="150" y="648" font-size="11" text-anchor="middle">7g High Quality</text>
    <text class="serif ink" x="150" y="660" font-size="11" text-anchor="middle">Protein</text>
    <text class="serif ink" x="150" y="691" font-size="9" text-anchor="middle">Alcohol percentage:</text>
    <text class="serif ink" x="150" y="701" font-size="9" text-anchor="middle">4%/Vol</text>
    <text class="serif ink" x="150" y="742" font-size="12" text-anchor="middle">Volume: 300ml</text>
  </g>

  <!-- Honey Ale label -->
  <g class="label label-honey">
    <rect x="378" y="510" width="144" height="30" fill="var(--honey-band)"/>
    <text class="sans-light honey-ink" x="450" y="531" font-size="15" text-anchor="middle">Gravel Ale</text>
    <polygon points="380,612 400,590 500,590 520,612 520,690 500,702 400,702 380,690" fill="var(--honey-fill)" stroke="var(--honey-line)" stroke-width="3"/>
    <rect x="425" y="603" width="50" height="15" fill="var(--honey-line)"/>
    <text class="sans-light" x="450" y="614" font-size="8" fill="#b8d8d6" text-anchor="middle">300 ml</text>
    <text class="sans-light honey-ink" x="450" y="653" font-size="27" text-anchor="middle">Honey Ale</text>
    <line x1="395" y1="665" x2="505" y2="665" stroke="var(--honey-line)" stroke-width="1"/>
    <text class="sans-light honey-ink" x="450" y="681" font-size="8" text-anchor="middle">7g High Quality Protein</text>
    <text class="sans-light honey-ink" x="450" y="692" font-size="6" text-anchor="middle">ALCOHOL PERCENTAGE: 4%/VOL</text>
  </g>

  <!-- Larger label -->
  <g class="label label-lager">
    <circle cx="750" cy="556" r="66" fill="var(--lager-blue)" stroke="var(--lager-ring)" stroke-width="5"/>
    <text class="sans-bold white" x="750" y="564" font-size="20" text-anchor="middle">Gravel Ale</text>
    <polygon points="682,631 815,631 806,657 682,657" fill="var(--lager-blue)"/>
    <text class="serif white" x="700" y="650" font-size="14" font-weight="700">Larger</text>
    <polygon points="682,668 815,668 806,691 682,691" fill="var(--lager-blue)"/>
    <text class="serif white" x="746" y="683" font-size="9" font-weight="700" text-anchor="middle">7g High Quality Protein</text>
    <polygon points="682,701 815,701 806,725 682,725" fill="var(--lager-blue)"/>
    <text class="serif white" x="746" y="718" font-size="12" font-weight="700" text-anchor="middle">Volume: 300ml</text>
    <polygon points="682,732 815,732 806,755 682,755" fill="var(--lager-blue)"/>
    <text class="serif white" x="746" y="748" font-size="10" font-weight="700" text-anchor="middle">Alcohol percentage:</text>
    <polygon points="682,763 815,763 806,787 682,787" fill="var(--lager-blue)"/>
    <text class="serif white" x="698" y="780" font-size="13" font-weight="700">4%/Vol</text>
  </g>

  <!-- Zero Alcohol label -->
  <g class="label label-zero">
    <circle cx="1050" cy="527" r="62" fill="none" stroke="var(--zero-red)" stroke-width="5" opacity=".85"/>
    <text class="sans-bold red" x="1050" y="522" font-size="22" text-anchor="middle">Gravel</text>
    <text class="sans-bold red" x="1050" y="548" font-size="22" text-anchor="middle">Ale</text>
    <rect class="zero-frame" x="988" y="588" width="124" height="30"/>
    <text class="serif red" x="1050" y="609" font-size="14" font-weight="700" text-anchor="middle">Zero Alcohol</text>
    <rect class="zero-frame" x="988" y="627" width="124" height="34"/>
    <text class="serif red" x="1050" y="648" font-size="10" font-weight="700" text-anchor="middle">7g High Quality Protein</text>
    <rect class="zero-frame" x="988" y="669" width="124" height="33"/>
    <text class="serif red" x="1050" y="690" font-size="8" font-weight="700" text-anchor="middle">Alcohol percentage: 0%/Vol</text>
    <rect class="zero-frame" x="988" y="711" width="124" height="35"/>
    <text class="serif red" x="1050" y="734" font-size="14" font-weight="700" text-anchor="middle">Volume: 300ml</text>
  </g>
</svg>
</body>
</html>
```